Just Sold flyer for Australian Real estate agent

We are looking for a catchy double-sided flyer. Can be either DL or A6<br/><br/>We would like to promote the recent sale of a stunning Federation style home for a fantastic sale price<br/>Details as follows - images attached<br/>4 Tilbury Avenue, Bardwell Valley<br/>3 bed 2 bath 1 car<br/>SOLD by Lou Brennick <br/> 0491 570 234<br/>Sale Price $1,309,500<br/><br/>At the same time, we would also like to promote Lou Brennick and our Agencies services whilst offering "Free Market appraisal" <br/>Thinking of Selling? - We have qualified buyers ready<br/><br/>Details -<br/>Agency - Kestrel Property Agents<br/>kestrelpropertyagents.com.au<br/>02 9613 4751<br/>Lou Brennick - Principal / LREA<br/>lou@kestrelpa.com.au<br/>0491 570 234<br/><br/><br/>Office colours <br/>Green<br/>CMYK - 61-0-96-0<br/>Blue<br/>CMYK - 100-88-27-19<br/><br/>Look forward to seeing your designs!

```html
<!DOCTYPE html>
<html lang="en">
<head>
<meta charset="utf-8">
<title>Kestrel Property Agents – DL Flyer</title>
<link href="https://fonts.googleapis.com/css2?family=Montserrat:wght@400;600;700;800&family=Oswald:wght@500;600&display=swap" rel="stylesheet">
<style>
  :root{
    --navy:#1d2f6b;
    --navy-deep:#14237a;
    --green:#5cb83c;
    --paper:#ffffff;
    --stage:#e5e5e5;
    --ink:#222;
  }
  *{box-sizing:border-box;margin:0;padding:0}
  html,body{width:900px;height:1200px;overflow:hidden;background:var(--stage)}
  .canvas{position:relative;width:900px;height:1200px}
  .flyer{position:absolute;top:190px;width:390px;height:820px;background:var(--paper);overflow:hidden;box-shadow:0 4px 14px rgba(0,0,0,.25);font-family:'Montserrat',sans-serif;color:var(--ink)}
  .flyer--front{left:40px}
  .flyer--back{left:470px}
  .flyer svg.shapes{position:absolute;inset:0;width:390px;height:820px}
  .abs{position:absolute;left:0;width:100%;text-align:center}
  .headline{position:absolute;left:18px;top:14px;font-family:'Oswald',sans-serif;font-weight:600;font-size:50px;color:#fff;letter-spacing:-.5px;line-height:1}
  .agency-name{display:inline-flex;align-items:center;gap:8px;font-weight:800;color:var(--navy);line-height:1.1}
  .agency-name::before{content:"";width:12px;height:12px;background:var(--navy);flex:none}
  .agency-name--front{font-size:25px}
  .agency-name--back{position:absolute;left:26px;top:446px;width:190px;font-size:20px;align-items:flex-start}
  .agency-name--back::before{margin-top:5px}
  .intro{font-size:11.5px;line-height:1.45;color:#333;padding:0 30px}
  .offer{font-weight:800;color:var(--green);font-size:27px;line-height:1.1}
  .price-tag{position:absolute;left:129px;top:678px;width:132px;height:33px;background:var(--navy);color:#fff;font-family:'Oswald',sans-serif;font-weight:500;font-size:20px;text-align:center;line-height:33px}
  .price{font-family:'Oswald',sans-serif;font-weight:500;color:var(--green);font-size:46px;line-height:1}
  .footer-text{color:#fff;font-size:12.5px;line-height:1}
  .contact-box{position:absolute;left:23px;top:537px;width:344px;height:219px;border:2px solid var(--navy);border-radius:10px;background:rgba(255,255,255,.85)}
  .ask{font-weight:800;color:var(--green);font-size:23px;line-height:1}
  .ready{font-weight:600;font-size:13px;color:#222}
  .agency{font-weight:700;color:var(--green);font-size:16px}
  .agent{font-weight:800;color:var(--navy);font-size:24px;line-height:1}
  .role,.email{font-size:12.5px;color:#333}
  .phone{font-weight:700;font-size:15px;color:#111}
  .call{color:#fff;font-size:16px;line-height:1}
  .call b{font-weight:800}
</style>
</head>
<body>
<div class="canvas">

  <section class="flyer flyer--front">
    <svg class="shapes" viewBox="0 0 390 820">
      <defs>
        <linearGradient id="sky" x1="0" y1="0" x2="0" y2="1">
          <stop offset="0" stop-color="#1f8fe6"/>
          <stop offset=".45" stop-color="#8fc4ef"/>
          <stop offset=".65" stop-color="#a65a3e"/>
          <stop offset=".85" stop-color="#e8e4dc"/>
          <stop offset="1" stop-color="#8a9a6a"/>
        </linearGradient>
        <linearGradient id="faint" x1="0" y1="0" x2="0" y2="1">
          <stop offset="0" stop-color="#f4f4f4"/>
          <stop offset="1" stop-color="#e9e9e9"/>
        </linearGradient>
      </defs>
      <rect x="0" y="30" width="390" height="396" fill="url(#sky)" role="img" aria-label="Photo of a red-brick Federation style home behind a white picket fence under a blue sky"/>
      <rect x="0" y="434" width="390" height="386" fill="url(#faint)" role="img" aria-label="Faded interior photo of the home behind the text"/>
      <polygon points="0,0 390,0 390,61 273,37 159,91 0,91" fill="var(--navy)"/>
      <polyline points="0,94 159,94 273,40 390,64" fill="none" stroke="var(--green)" stroke-width="6"/>
      <rect x="0" y="424" width="390" height="8" fill="var(--navy)"/>
      <polygon points="30,785 360,785 390,820 0,820" fill="var(--navy-deep)"/>
    </svg>
    <div class="headline">JUST SOLD</div>
    <div class="abs" style="top:500px"><span class="agency-name agency-name--front">Kestrel Property Agents</span></div>
    <p class="abs intro" style="top:560px">At the same time, we would also like to promote Lou Brennick and our Agencies services whilst offering</p>
    <div class="abs offer" style="top:598px">FREE MARKET<br>APPRAISAL</div>
    <div class="price-tag">SALE PRICE</div>
    <div class="abs price" style="top:722px">$1,309,500</div>
    <div class="abs footer-text" style="top:798px">www.kestrelpropertyagents.com.au</div>
  </section>

  <section class="flyer flyer--back">
    <svg class="shapes" viewBox="0 0 390 820">
      <defs>
        <linearGradient id="room" x1="0" y1="0" x2="0" y2="1">
          <stop offset="0" stop-color="#ededed"/>
          <stop offset=".45" stop-color="#e6dcd6"/>
          <stop offset=".7" stop-color="#d9b8b0"/>
          <stop offset="1" stop-color="#8a4a2a"/>
        </linearGradient>
        <linearGradient id="lounge" x1="0" y1="0" x2="0" y2="1">
          <stop offset="0" stop-color="#e8e8e8"/>
          <stop offset="1" stop-color="#7a4a36"/>
        </linearGradient>
      </defs>
      <rect x="0" y="0" width="390" height="430" fill="url(#room)" role="img" aria-label="Photo of a bedroom with a white bed, cushions and timber floor"/>
      <rect x="0" y="430" width="390" height="390" fill="#f3f3f3" role="img" aria-label="Faded photo of a picket fence behind the contact details"/>
      <polygon points="0,430 110,366 290,420 390,425 390,820 0,820" fill="#fff"/>
      <polyline points="0,425 110,363 290,416 390,421" fill="none" stroke="var(--green)" stroke-width="10"/>
      <polygon points="291,352 361,392 361,474 291,514 221,474 221,392" fill="url(#lounge)" stroke="var(--navy)" stroke-width="4" role="img" aria-label="Photo of a living room with fireplace"/>
      <polygon points="0,784 390,784 370,820 20,820" fill="var(--navy-deep)"/>
    </svg>
    <span class="agency-name agency-name--back">Kestrel Property Agents</span>
    <div class="contact-box"></div>
    <div class="abs ask" style="top:556px">THINKING OF SELLING?</div>
    <div class="abs ready" style="top:581px">We have qualified buyers ready</div>
    <div class="abs agency" style="top:617px">Kestrel Property Agents</div>
    <div class="abs agent" style="top:660px">LOU BRENNICK</div>
    <div class="abs role" style="top:684px">Principal</div>
    <div class="abs email" style="top:702px">lou@kestrelpa.com.au</div>
    <div class="abs phone" style="top:720px">0491 570 234</div>
    <div class="abs call" style="top:795px">CALL US NOW: <b>02 9613 4751</b></div>
  </section>

</div>
</body>
</html>
```